VELTRIX Web Page

We need a corporate web site for a new company VELTRIX Corporation. VELTRIX is a technology company that has developed a new virtualization solution for corporate applications. Our target customers are IT professionals. We have a logo, which we will provide.

Final design should communicate: innovation, stability, professionalism

Industry/Entity Type

It Company

```html
<!DOCTYPE html>
<html lang="en">
<head>
<meta charset="utf-8">
<title>VELTRIX Corporation</title>
<link href="https://fonts.googleapis.com/css2?family=Arimo:wght@400;700&family=Questrial&family=Nunito:wght@800&family=Pathway+Gothic+One&display=swap" rel="stylesheet">
<style>
:root{
  --blue:#0a7dbd;
  --blue-dark:#066aa3;
  --green:#a4c31f;
  --green-light:#b8d02a;
  --text:#222;
  --muted:#555;
  --white:#fff;
  --footer-link:#d5e96a;
}
*{margin:0;padding:0;box-sizing:border-box}
html,body{width:784px;height:1200px;overflow:hidden;background:var(--white)}
body{position:relative;font-family:"Arimo",Arial,sans-serif;color:var(--text)}
.header{position:absolute;left:0;top:0;width:784px;height:82px;background:var(--blue)}
.logo{position:absolute;left:12px;top:6px;width:133px;height:69px;border-radius:50%;background:linear-gradient(#fff,#e4e8ee);box-shadow:0 2px 4px rgba(0,0,0,.3);display:flex;align-items:center;justify-content:center;font-weight:700;font-size:19px;color:var(--blue-dark);letter-spacing:.5px}
.tagline{position:absolute;left:245px;top:28px;font-family:"Pathway Gothic One",sans-serif;font-size:24px;color:var(--white)}
.tagline b{font-weight:400;font-size:25px;letter-spacing:.3px;text-shadow:0 0 .6px #fff}
.call{position:absolute;right:17px;top:15px;text-align:right;color:var(--white)}
.call small{display:block;font-size:14px}
.call .num{display:flex;align-items:center;gap:6px;font-family:"Pathway Gothic One",sans-serif;font-size:30px;line-height:32px}
.nav{position:absolute;left:0;top:86px;width:784px;height:33px;background:var(--green)}
.nav a{position:absolute;top:0;height:33px;line-height:33px;color:var(--white);font-size:13px;text-decoration:none}
.nav a.active{background:var(--blue);width:85px;left:10px;text-align:center}
.hero{position:absolute;left:0;top:119px;width:784px;height:305px;background:radial-gradient(ellipse at 50% 45%,#7a8fa8 0%,#35567a 45%,#1c3656 100%)}
.why{position:absolute;left:24px;top:448px;width:400px}
h2{font-family:"Questrial",sans-serif;font-weight:400;color:var(--blue);font-size:31px}
.why p{margin-top:20px;font-size:9.3px;line-height:11.7px;color:var(--text)}
.checks{list-style:none;margin-top:13px}
.checks li{display:flex;align-items:center;gap:10px;height:20.3px;font-size:9.4px;margin-left:9px}
.news{position:absolute;left:528px;top:448px;width:211px;height:240px}
.item{position:relative;height:61px;border-bottom:1px dotted #999;margin-bottom:27px}
.item:first-of-type{margin-top:12px}
.date{position:absolute;left:2px;top:2px;width:28px;text-align:center}
.date .d{width:25px;height:25px;margin:0 auto;border-radius:50%;background:var(--blue);border:2px solid #bfe0f2;color:#fff;font-family:"Pathway Gothic One",sans-serif;font-size:16px;line-height:21px}
.date .m{color:var(--blue);font-size:9.5px;font-weight:700;margin-top:3px}
.item .body{position:absolute;left:48px;top:2px;width:165px}
.item h4{font-size:9.5px;font-weight:700;color:var(--text)}
.item p{font-size:8.2px;color:var(--muted);margin-top:6px;line-height:10.5px}
.more{color:var(--green);font-size:8.2px;font-weight:700;margin-top:2px}
.all{position:absolute;right:0;top:221px;color:var(--green);font-size:8.6px}
.feature{position:absolute;top:750px;width:204px}
.badge{position:relative;width:90px;height:70px}
.badge .back{position:absolute;left:21px;top:0;width:70px;height:70px;border-radius:50%;background:var(--green-light)}
.badge .front{position:absolute;left:0;top:0;width:68px;height:68px;border-radius:50%;background:var(--blue);display:flex;align-items:center;justify-content:center}
.feature h3{font-family:"Nunito",sans-serif;font-weight:800;font-size:14.5px;color:var(--blue);margin-top:14px}
.feature p{font-size:8.8px;line-height:11.6px;color:var(--muted);margin-top:8px}
.feature .rm{font-size:8.6px;font-weight:700;color:var(--muted);margin-top:6px}
.partners{position:absolute;left:0;top:980px;width:784px;height:86px;overflow:hidden;background:linear-gradient(#f2f2f2,#fff 12%,#fff 88%,#f2f2f2)}
.arrow{position:absolute;top:22px;font-size:32px;color:#666;font-family:"Questrial",sans-serif}
.brand{position:absolute;top:0;height:86px;display:flex;align-items:center;gap:5px;font-weight:700;font-size:15px;color:#3a4a5a;white-space:nowrap}
.brand i{display:block;width:11px;height:11px;border-radius:50%;background:var(--blue)}
.footer{position:absolute;left:0;top:1105px;width:784px;height:95px;background:var(--blue);text-align:center}
.social{display:flex;justify-content:center;gap:8px;margin-top:15px}
.social span{width:20px;height:20px;border-radius:50%;background:var(--white);display:flex;align-items:center;justify-content:center}
.rule{width:620px;height:1px;background:#2b92c9;margin:12px auto 0}
.links{margin-top:8px;font-size:9.5px;color:var(--footer-link)}
.links a{color:inherit;text-decoration:none;margin:0 2px}
.copy{margin-top:5px;font-size:8px;color:#7fc0e3}
</style>
</head>
<body>
<header class="header">
  <div class="logo">VELTRIX</div>
  <div class="tagline">Virtualization Solution for <b>IT Professionals</b></div>
  <div class="call"><small>Toll free call now!</small>
    <div class="num">
      <svg width="26" height="26" viewBox="0 0 26 26"><circle cx="13" cy="13" r="11.5" fill="none" stroke="#fff" stroke-width="2"/><path d="M9 7l2.5 3-1.5 1.5c.8 2 2.5 3.7 4.5 4.5L16 14.5l3 2.5-1.5 2.5C12 19 7 14 6.5 8.5z" fill="#fff"/></svg>
      0198 765 432</div>
  </div>
</header>
<nav class="nav">
  <a class="active" href="#">Home</a>
  <a href="#" style="left:140px">Services</a>
  <a href="#" style="left:257px">Solutions</a>
  <a href="#" style="left:380px">Partners</a>
  <a href="#" style="left:493px">About Us</a>
  <a href="#" style="left:614px">Contact</a>
</nav>
<div class="hero" role="img" aria-label="Hand touching glowing virtual interface circles over a world map"></div>

<section class="why">
  <h2>Why VELTRIX</h2>
  <p>Lorem ipsum dolor sit amet, consectetur adipisicing elit, sed do eiusmod tempor incididunt ut l abore et dolore magna aliqua. Ut enim ad minim veniam, quis nostrud exercitation ullamco laboris nisi ut aliquip ex ea commodo consequat. Duis aute irure dolor in reprehenderit in voluptate velit esse cillum dolore eu fugiat nulla pariatur. Excepteur sint occaecat cupidatat non proident, sunt in culpa qui officia deserunt mollit anim id est laborum.</p>
  <ul class="checks">
    <li><svg width="13" height="13" viewBox="0 0 13 13"><circle cx="6.5" cy="6.5" r="6" fill="#2d3a2a"/><path d="M3 6.5l2.5 2.5L11 2.5" stroke="#7cc21f" stroke-width="2.2" fill="none"/></svg>Sed ut perspiciatis, unde omnis iste natus error sit voluptatem accusantium</li>
    <li><svg width="13" height="13" viewBox="0 0 13 13"><circle cx="6.5" cy="6.5" r="6" fill="#2d3a2a"/><path d="M3 6.5l2.5 2.5L11 2.5" stroke="#7cc21f" stroke-width="2.2" fill="none"/></svg>Doloremque laudantium, totam rem aperiam eaque ipsa, quae ab illo inventore</li>
    <li><svg width="13" height="13" viewBox="0 0 13 13"><circle cx="6.5" cy="6.5" r="6" fill="#2d3a2a"/><path d="M3 6.5l2.5 2.5L11 2.5" stroke="#7cc21f" stroke-width="2.2" fill="none"/></svg>Veritatis et quasi architecto beatae vitae dicta sunt, explicabo.</li>
    <li><svg width="13" height="13" viewBox="0 0 13 13"><circle cx="6.5" cy="6.5" r="6" fill="#2d3a2a"/><path d="M3 6.5l2.5 2.5L11 2.5" stroke="#7cc21f" stroke-width="2.2" fill="none"/></svg>Nemo enim ipsam voluptatem, quia voluptas sit, aspernatur aut odit aut fugit</li>
    <li><svg width="13" height="13" viewBox="0 0 13 13"><circle cx="6.5" cy="6.5" r="6" fill="#2d3a2a"/><path d="M3 6.5l2.5 2.5L11 2.5" stroke="#7cc21f" stroke-width="2.2" fill="none"/></svg>Quia consequuntur magni dolores eos, qui ratione voluptatem sequi nesciunt</li>
  </ul>
</section>

<aside class="news">
  <h2>Latest News</h2>
  <div class="item">
    <div class="date"><div class="d">07</div><div class="m">AUG</div></div>
    <div class="body"><h4>Lorem ipsum dolor sit amet</h4><p>Lorem ipsum dolor sit amet, consectetur adipisicing elit, sed do.</p><div class="more">read more +</div></div>
  </div>
  <div class="item">
    <div class="date"><div class="d">07</div><div class="m">AUG</div></div>
    <div class="body"><h4>Lorem ipsum dolor sit amet</h4><p>Lorem ipsum dolor sit amet, consectetur adipisicing elit, sed do.</p><div class="more">read more +</div></div>
  </div>
  <div class="all">more news +</div>
</aside>

<div class="feature" style="left:31px">
  <div class="badge"><div class="back"></div><div class="front">
    <svg width="38" height="38" viewBox="0 0 38 38"><path d="M9 22a6 6 0 0 1 1-12 9 9 0 0 1 17 2 5 5 0 0 1 0 10z" fill="#fff"/><path d="M12 26q7 4 14 0M14 30q5 3 10 0M16 34q3 1.5 6 0" stroke="#fff" stroke-width="1.8" fill="none"/></svg></div></div>
  <h3>At Vero Eos Et</h3>
  <p>Xos et accusamus et iusto odio dignissimos ducimus, qui blanditiis praesentium voluptatum deleniti atque corrupti, quos dolores et quas molestias excepturi</p>
  <div class="rm">read more +</div>
</div>
<div class="feature" style="left:287px">
  <div class="badge"><div class="back"></div><div class="front">
    <svg width="38" height="30" viewBox="0 0 38 30"><rect x="7" y="3" width="24" height="17" rx="2" fill="#fff"/><rect x="2" y="22" width="34" height="4" rx="1.5" fill="#fff"/></svg></div></div>
  <h3>IT Accusamus Et Iusto</h3>
  <p>Et harum quidem rerum facilis est et expedita distinctio. Nam libero tempore, cum soluta nobis est eligendi optio, cumque nihil impedit, quo minus id, quod maxime placeat, facere</p>
  <div class="rm">read more +</div>
</div>
<div class="feature" style="left:543px">
  <div class="badge"><div class="back"></div><div class="front">
    <svg width="34" height="34" viewBox="0 0 34 34"><circle cx="17" cy="10" r="6" fill="#fff"/><path d="M4 31c0-9 5-12 13-12s13 3 13 12z" fill="#fff"/></svg></div></div>
  <h3>Dignissimos Ducimus</h3>
  <p>qui dolorem ipsum, quia dolor sit amet, conse adipisci[ng] velit, sed quia non numquam [do] modi tempora inci[di]dunt, ut labore et dolore magnam aliquam quaerat voluptatem.</p>
  <div class="rm">read more +</div>
</div>

<div class="partners">
  <div class="arrow" style="left:6px">&#8249;</div>
  <div class="brand" style="left:44px"><i></i>Northline</div>
  <div class="brand" style="left:180px">Corvex</div>
  <div class="brand" style="left:284px">Stratacore</div>
  <div class="brand" style="left:398px">Paylo</div>
  <div class="brand" style="left:456px"><i></i>Voltana</div>
  <div class="brand" style="left:556px"><i></i>Sciora</div>
  <div class="brand" style="left:646px">Meridex</div>
  <div class="arrow" style="left:760px">&#8250;</div>
</div>

<footer class="footer">
  <div class="social">
    <span><svg width="11" height="11" viewBox="0 0 11 11"><path d="M1 2h9v5H5L3 9V7H1z" fill="#0a7dbd"/></svg></span>
    <span><svg width="11" height="11" viewBox="0 0 11 11"><rect x="1" y="2.5" width="9" height="6" fill="#0a7dbd"/><path d="M1 2.5l4.5 3.5 4.5-3.5" stroke="#fff" stroke-width="1" fill="none"/></svg></span>
    <span><svg width="11" height="11" viewBox="0 0 11 11"><circle cx="5.5" cy="5.5" r="4.3" fill="none" stroke="#0a7dbd" stroke-width="1.3"/><path d="M1.2 5.5h8.6M5.5 1.2q-3 4.3 0 8.6M5.5 1.2q3 4.3 0 8.6" stroke="#0a7dbd" stroke-width="1" fill="none"/></svg></span>
    <span><svg width="11" height="11" viewBox="0 0 11 11"><circle cx="2.5" cy="5.5" r="1.6" fill="#0a7dbd"/><circle cx="8.5" cy="2.5" r="1.6" fill="#0a7dbd"/><circle cx="8.5" cy="8.5" r="1.6" fill="#0a7dbd"/><path d="M2.5 5.5L8.5 2.5M2.5 5.5L8.5 8.5" stroke="#0a7dbd" stroke-width="1"/></svg></span>
    <span><svg width="11" height="11" viewBox="0 0 11 11"><path d="M5.5 1.5a3 3 0 0 1 3 3v2.5l1 1.5h-8l1-1.5V4.5a3 3 0 0 1 3-3z" fill="#0a7dbd"/><circle cx="5.5" cy="9.6" r="1" fill="#0a7dbd"/></svg></span>
  </div>
  <div class="rule"></div>
  <div class="links"><a href="#">Home</a> <a href="#">Services</a> <a href="#">Solutions</a> <a href="#">Partners</a> <a href="#">About Us</a> <a href="#">Contact</a></div>
  <div class="copy">© Copyright 2013 VELTRIX. All Rights Reserved</div>
</footer>
</body>
</html>
```